Investment Company Business Card Design

We need a Business Card design for a new company based in Boston called "Olt Investment". We are cooperating with local real estate and construction companies. Our company is very actively and aggressively acquiring primarily residential investment properties either to buy and hold long term or for purposes or renovating and repositioning for re-sale in the market. In addition, we undertake some development projects and acquisitions as opportunities present themselves. the final design should contains information about “Olt" the river boat. we are tenacious, indomitable, and the business have a favorable wind throughout the voyage for all our investment.
sample Info. on Design:
Tem Hollis
CEO
508-xxx-xxxx
415 Marrow St. Suite 108, Boston, MA 02127
Please provide a template also, that we can edit the info later.
Reason: i just got new LOGO Design attached will be use in Business Card Design.
Construction

```html
<!DOCTYPE html>
<html lang="en">
<head>
<meta charset="utf-8">
<title>Olt Investment Business Card</title>
<link rel="stylesheet" href="https://fonts.googleapis.com/css2?family=Mulish:wght@400;700;800&display=swap">
<style>
  :root {
    --backdrop: #e4e4e4;
    --card-top: #3a3a3a;
    --card-bottom: #1c1c1c;
    --gold: #d1a56c;
    --gold-deep: #b8895a;
    --grey-text: #a9a9a9;
    --shadow: rgba(0, 0, 0, 0.35);
  }
  * { box-sizing: border-box; margin: 0; padding: 0; }
  html, body {
    width: 1200px;
    height: 720px;
    overflow: hidden;
    background: var(--backdrop);
    font-family: "Mulish", "Century Gothic", sans-serif;
  }
  .canvas {
    position: relative;
    width: 1200px;
    height: 720px;
  }
  .card {
    position: absolute;
    top: 241px;
    width: 419px;
    height: 239px;
    background: linear-gradient(160deg, var(--card-top) 0%, #2a2a2a 45%, var(--card-bottom) 100%);
    box-shadow: 0 14px 24px var(--shadow);
    overflow: hidden;
  }
  .card--front { left: 147px; }
  .card--back { left: 633px; }

  .brand-name {
    position: absolute;
    color: var(--gold);
    font-weight: 700;
    white-space: nowrap;
    letter-spacing: 0.02em;
  }
  .card--front .brand-name {
    left: 0;
    right: 0;
    top: 100px;
    text-align: center;
    font-size: 32px;
  }
  .card--back .brand-name {
    right: 26px;
    top: 62px;
    font-size: 19px;
  }

  .holder-name {
    position: absolute;
    left: 15px;
    top: 106px;
    color: var(--gold);
    font-size: 19px;
    font-weight: 800;
  }
  .holder-role {
    position: absolute;
    left: 15px;
    top: 133px;
    color: var(--grey-text);
    font-size: 12px;
    letter-spacing: 0.04em;
  }
  .contact {
    position: absolute;
    left: 15px;
    top: 182px;
    color: var(--gold);
    font-size: 12px;
    line-height: 18px;
  }
  .motto {
    position: absolute;
    left: 222px;
    width: 200px;
    top: 119px;
    color: var(--grey-text);
    font-size: 10.5px;
    line-height: 19.5px;
    text-align: center;
  }
</style>
</head>
<body>
<main class="canvas">
  <section class="card card--front" aria-label="Card front">
    <div class="brand-name">Olt Investment</div>
  </section>

  <section class="card card--back" aria-label="Card back">
    <div class="brand-name">Olt Investment</div>
    <h1 class="holder-name">Tem Hollis</h1>
    <p class="holder-role">CEO</p>
    <address class="contact">
      508-xxx-xxxx<br>
      415 Marrow St. Suite 108, Boston, MA
    </address>
    <p class="motto">we are tenacious, indomitable, and the business have a favorable wind throughout the voyage for all our investment.</p>
  </section>
</main>
</body>
</html>
```